Zielgruppe
Wir sind eine Wäscherei.
Zielgruppe: Kunden aus der Hotel- und Gastronomiebranche
Aufgabenstellung
Wir benötigen einen 2-seitigen Flyer DIN lang. 9,8 x21cm
TextInhalte sind in der Vorlage-Datei.
Bilder sind eingefügt.

```html
<!DOCTYPE html>
<html lang="de">
<head>
<meta charset="utf-8">
<title>Wäscherei Kellermann – Serviettenfaltservice</title>
<link rel="stylesheet" href="https://fonts.googleapis.com/css2?family=Open+Sans:wght@400;700&family=Pinyon+Script&display=swap">
<style>
  :root {
    --magenta: #e620e0;
    --ink: #1e1e1e;
    --header-top: #f2f2f2;
    --header-bottom: #fbfbfb;
    --panel-light: #fdfdfd;
    --panel-mist: #eeeeee;
    --photo-light: #e9ecec;
    --photo-mid: #c9cfcf;
    --photo-dark: #8e9494;
  }
  * { margin: 0; padding: 0; box-sizing: border-box; }
  html, body { width: 1200px; height: 560px; overflow: hidden; background: #ffffff; }
  .flyer {
    position: relative;
    width: 1200px;
    height: 560px;
    overflow: hidden;
    font-family: "Open Sans", Arial, sans-serif;
    color: var(--ink);
    background: linear-gradient(180deg, var(--panel-light) 0%, #f7f7f7 100%);
  }
  .header {
    position: absolute;
    left: 0; top: 0;
    width: 1200px; height: 131px;
    background: linear-gradient(180deg, var(--header-top), var(--header-bottom));
    border-bottom: 1px solid #e6e6e6;
  }
  .contact-line {
    position: absolute;
    left: 57px; top: 67px;
    font-size: 14.3px;
    letter-spacing: 0.1px;
    white-space: nowrap;
  }
  .brand {
    position: absolute;
    right: 32px; top: 62px;
    display: flex; align-items: center; gap: 8px;
    font-size: 21px;
    font-weight: 700;
    color: var(--magenta);
    letter-spacing: 0.5px;
    white-space: nowrap;
  }
  .brand-dot {
    width: 12px; height: 12px;
    background: var(--magenta);
    border-radius: 50%;
  }
  .left-mist {
    position: absolute;
    left: 0; top: 132px;
    width: 542px; height: 428px;
    background: radial-gradient(ellipse at 75% 30%, var(--panel-mist) 0%, var(--panel-light) 65%);
  }
  .table-photo {
    position: absolute;
    left: 542px; top: 132px;
    width: 658px; height: 428px;
    background:
      linear-gradient(160deg, var(--photo-light) 0%, #f4f6f6 45%, var(--photo-mid) 85%, var(--photo-dark) 100%);
  }
  .launch-date {
    position: absolute;
    left: 53px; top: 167px;
    font-size: 18.5px;
  }
  .service-title {
    position: absolute;
    left: 40px; top: 205px;
    font-family: "Pinyon Script", cursive;
    font-size: 66px;
    color: var(--magenta);
    white-space: nowrap;
  }
  .service-list {
    position: absolute;
    left: 57px; top: 360px;
    list-style: none;
    font-size: 18.5px;
    line-height: 24.2px;
  }
</style>
</head>
<body>
  <div class="flyer">
    <header class="header">
      <p class="contact-line">Wäscherei Kellermann • Lindenweg 14 • 71990 Talbach • Tel. +49 (0) 7190 / 36 52 10 • info@waescherei-kellermann.de</p>
      <div class="brand"><span class="brand-dot"></span>WÄSCHEREI KELLERMANN</div>
    </header>

    <div class="left-mist" role="img" aria-label="Blass ausgeblendete Fortsetzung des festlich gedeckten Tisches mit Gläsern und Gabeln"></div>
    <div class="table-photo" role="img" aria-label="Foto eines runden, weiß eingedeckten Tisches mit gefalteten Stoffservietten, Weingläsern, Besteck, Salz- und Pfefferstreuer und Blumengesteck"></div>

    <p class="launch-date">ab November 2017</p>
    <h1 class="service-title">Serviettenfaltservice</h1>

    <ul class="service-list">
      <li>Hotel- und Gastronomiewäsche</li>
      <li>Schmutzmatten</li>
      <li>Gardinenservice</li>
      <li>Berufskleidung</li>
      <li>Private Wäsche</li>
      <li>Verkauf von Hotel- und Gastronomietextilien</li>
    </ul>
  </div>
</body>
</html>
```